Southern Grain Assurance- Web & Business card design for a new business within the Ag Sector

HELLO!!!!

We need your help in relation to web design (business cards and stationary if possible!) for a new company based in NSW, Australia.

The name of the business is: Southern Grain Assurance (SGA). I have quickly mocked a webpage just to give you an idea of what we are looking for.... http://fieldmockup7.sitebuildly.example/http

SGA is a strategic advisory, investment manager and problem solver within the Australian Agricultural sector.

Our Mission:

We are here to provide solutions to ALL of our Clients needs and desires within the Agricultural space.

Our Team:

Our team has worked with some of the largest & oldest Agricultural companies in Australia

We provide our Clients with a unique blend of the best Corporate as well as Operational experience that the Industry has to offer.

Client-driven Services Approach:

SGA offers a tailored service in order to meet the objectives and outcomes for each and every client.

Some of our services include:

- Food Security / Supply

- Procurement strategies within and across agricultural supply-chains

- Strategic Agribusiness advice for both Australian and Chinese based agricultural enterprises

- M&A / Due Diligence

- Corporate governance & risk management strategies.

I have attached a copy of our capability statement for background reading.

We look forward to receiving your designs!!!!!!!
Updates

Target Market(s)

Corporate, Family Offices, Food Services & Supermarkets - that are looking to obtain products within the agricultural space. Whether it be boxed beef, grain, live animals, advice - ie M&A, Due diligence - just think anything "Agricultural" and we can provide a solution

Industry/Entity Type

Agriculture

Contact Information for Business Card

See below

With respect to the business cards:

There are 2 Managing Directors:

1. Martin Pellow
Managing Director
E: martin.pellow@southerngrainassurance.example
M: +61 491 203 664
W: www.southerngrainassurance.example

2. Kate Wrenley
Managing Director
E: kate.wrenley@southerngrainassurance.example
M: +61 432 796 018

Please see attached 2 * Files named Brenmoor that outline a layout of business card that I like

Coding

Coded - Design and coding required

Number of Pages Required

5+ page

Font styles to use
Sans Serif
Other font styles liked:
• Calibri

Requirements
Must have
• I like the look of this website: http://pastoralvx.example/
• And I like the themes in the website that I have mocked up: http://fieldmockup7.sitebuildly.example/http
• The wow factor, with a professional twist.
• With respect to the website - would like it to follow the flow of the capability statement - ie with a home page, and the four additional pages:
• ABOUT US
• OUR SERVICES
• OUR TEAM
• CONTACT DETAILS
• The powerpoint presentation that I have attached is simply there for content direction - not design direction.
• As a result, am looking for web design / business card that stands out - is corporate - yet still agricultural feel.
• "capability statement" simply refers to a document that outlines our capabilities - and does not form part of the business name.
• A black angus cow, or a stalk of wheat - greens and yellows may better represent the Ag space.
• This s a draft mock-up of a web-site I created with one of those free web-page makers... This should give you a feel - crisp - whites - yet agricultural tones to highlight
• The attachments below should be used as inspiration - and don't need to be the actual shots used.

```html
<!DOCTYPE html>
<html lang="en">
<head>
<meta charset="utf-8">
<title>Southern Grain Assurance</title>
<link rel="stylesheet" href="https://fonts.googleapis.com/css2?family=Carlito:wght@400;700&display=swap">
<style>
  :root {
    --nav-bg: #07303f;
    --nav-text: #e4ecef;
    --accent-lime: #d3f09b;
    --accent-lime-text: #0c3a48;
    --dropdown-bg: rgba(14, 58, 76, 0.94);
    --sand: #dcd6c2;
    --ink: #0d0d0d;
    --brand-ink: #103c4a;
    --field-green: #22b573;
    --arrow-bg: rgba(70, 70, 70, 0.72);
  }
  * { box-sizing: border-box; margin: 0; padding: 0; }
  html, body {
    width: 1200px; height: 970px; overflow: hidden;
    font-family: "Carlito", "Calibri", sans-serif;
    background: #ffffff;
  }
  .page { position: relative; width: 1200px; height: 970px; overflow: hidden; }

  .site-header {
    position: absolute; top: 0; left: 0; width: 1200px; height: 72px;
    background: var(--nav-bg); z-index: 3;
    box-shadow: 0 2px 3px rgba(0,0,0,0.25);
  }
  .header-brand {
    position: absolute; left: 46px; top: 16px;
    display: flex; align-items: center; gap: 7px;
    color: var(--nav-text); font-size: 17px; font-weight: 700; letter-spacing: 1px;
  }
  .header-brand .mark { width: 16px; height: 16px; background: var(--nav-text); }
  .main-nav a {
    position: absolute; top: 0; height: 72px; line-height: 74px;
    color: var(--nav-text); font-size: 19px; text-decoration: none; white-space: nowrap;
    transform: translateX(-50%);
  }
  .main-nav .is-active {
    left: 694.5px; width: 171px; background: var(--accent-lime); color: var(--accent-lime-text);
    padding-left: 14px; text-align: left;
  }
  .main-nav .is-active svg { position: absolute; right: 15px; top: 30px; }

  .services-menu {
    position: absolute; left: 474px; top: 72px; width: 306px; height: 213px;
    background: var(--dropdown-bg); border-radius: 0 0 5px 5px; z-index: 3;
  }
  .services-menu a {
    position: absolute; left: 0; width: 306px; height: 37px; line-height: 37px;
    padding-left: 13px; color: var(--nav-text); font-size: 17.5px; text-decoration: none;
    transform: translateY(-50%);
  }
  .services-menu a.is-current { background: var(--accent-lime); color: var(--accent-lime-text); }

  .hero {
    position: absolute; top: 72px; left: 0; width: 1200px; height: 478px;
  }
  .hero-photo {
    position: absolute; inset: 0;
    background:
      radial-gradient(ellipse 260px 200px at 180px 340px, rgba(240,214,120,0.85), transparent 70%),
      radial-gradient(ellipse 220px 170px at 1030px 200px, rgba(236,214,120,0.8), transparent 70%),
      radial-gradient(ellipse 200px 120px at 660px 420px, rgba(240,172,40,0.7), transparent 70%),
      linear-gradient(135deg, #e6ecef 0%, #dfe6ea 50%, #e8ecec 100%);
  }
  .slider-arrow {
    position: absolute; top: 206px; width: 44px; height: 42px; background: var(--arrow-bg);
    display: flex; align-items: center; justify-content: center;
  }
  .slider-arrow.prev { left: 41px; }
  .slider-arrow.next { left: 1110px; }
  .slider-dots { position: absolute; top: 442px; left: 558px; display: flex; gap: 6px; }
  .slider-dots span {
    width: 14px; height: 14px; border-radius: 50%; border: 2px solid #ffffff;
  }
  .slider-dots span.is-on { background: #ffffff; }

  .intro {
    position: absolute; top: 550px; left: 0; width: 1200px; height: 331px;
    background: var(--sand); text-align: center;
  }
  .intro-brand {
    position: absolute; top: 30px; left: 0; width: 1200px;
    display: flex; flex-direction: column; align-items: center; gap: 18px;
    color: var(--brand-ink); font-weight: 700;
  }
  .intro-brand .mark { width: 70px; height: 70px; background: var(--brand-ink); }
  .intro-brand .name { font-size: 17px; line-height: 1.2; letter-spacing: 0.4px; }
  .intro-copy {
    position: absolute; top: 260px; left: 0; width: 1200px;
    font-size: 19px; line-height: 26px; color: var(--ink);
  }

  .feature-band {
    position: absolute; top: 881px; left: 0; width: 1200px; height: 89px;
    background: var(--field-green);
  }
  .feature-band h2 {
    position: absolute; left: 49px; top: 63px;
    font-size: 19px; font-weight: 700; color: var(--ink); letter-spacing: 0.2px;
  }
</style>
</head>
<body>
<div class="page">
  <header class="site-header">
    <div class="header-brand"><span class="mark"></span>SGA</div>
    <nav class="main-nav">
      <a href="#" style="left:367px">HOME</a>
      <a href="#" style="left:511px">ABOUT US</a>
      <a href="#" class="is-active">OUR SERVICES
        <svg width="13" height="9" viewBox="0 0 13 9"><path d="M1 1.5 L6.5 7 L12 1.5" fill="none" stroke="#0c3a48" stroke-width="1.6"/></svg>
      </a>
      <a href="#" style="left:864px">OUR TEAM</a>
      <a href="#" style="left:1056px">CONTACT DETAILS</a>
    </nav>
  </header>

  <div class="services-menu">
    <a href="#" style="top:31px">FOOD SECURITY / SUPPLY</a>
    <a href="#" class="is-current" style="top:72px">PROCUREMENT STRATEGY</a>
    <a href="#" style="top:113px">STRATEGIC AGRIBUSINESS ADVICE</a>
    <a href="#" style="top:149px">M &amp; A</a>
    <a href="#" style="top:187px">CORPORATE GOVERNANCE</a>
  </div>

  <section class="hero">
    <div class="hero-photo" role="img" aria-label="Flat-lay of fresh produce on a pale wooden table: lemons, ginger, bananas, quinces, yellow tomatoes, corn and lentils"></div>
    <div class="slider-arrow prev">
      <svg width="10" height="14" viewBox="0 0 10 14"><path d="M7 2 L2 7 L7 12" fill="none" stroke="#ffffff" stroke-width="1.6"/></svg>
    </div>
    <div class="slider-arrow next">
      <svg width="10" height="14" viewBox="0 0 10 14"><path d="M3 2 L8 7 L3 12" fill="none" stroke="#ffffff" stroke-width="1.6"/></svg>
    </div>
    <div class="slider-dots"><span class="is-on"></span><span></span><span></span></div>
  </section>

  <section class="intro">
    <div class="intro-brand">
      <span class="mark"></span>
      <div class="name">SOUTHERN GRAIN<br>ASSURANCE</div>
    </div>
    <p class="intro-copy">
      We are a strategic advisory, investment manager and problem solver with the Australian Agricultural sector.<br>
      We are here to provide solutions to ALL of our Clients needs and desires within the Agricultural space.
    </p>
  </section>

  <section class="feature-band">
    <h2>LOREM IPSUM DOLOR SIT AMET</h2>
  </section>
</div>
</body>
</html>
```